Letter Head, for use on daily correspondence with other companies

Hi

I want a professional Letter head, That my company can use to corresponded with other companies we do business with on a daily basis.

I want this done as soon as possible as this is peak session for us.

I have attached the company logo so please be creative and professional.
Kind regards

Marcus

Target Market(s)

All Audience searching for tickets, people in the entertainment world

Industry/Entity Type

Entertainment Industry

Font styles to use
Serif
Sans Serif
Decorative
Script

Requirements
Must have
• Very professional image.
• I will know want i want when i see it
• so please do your utmost in your professional standards
• Address of the company 24 hollin lane, telephone number 0207 562 3198
• Vat number: 487 2915 06.
• This letter head my be able to acomodate usage for directors & CEO as well as managers and employess
Nice to have
• A great professional image
Should not have
• Be creative please

```html
<!DOCTYPE html>
<html lang="en">
<head>
<meta charset="utf-8">
<title>Curtainline Tickets – Letterhead</title>
<link href="https://fonts.googleapis.com/css2?family=Merriweather:wght@400;700&display=swap" rel="stylesheet">
<style>
  :root {
    --brand-red: #e3222d;
    --paper: #ffffff;
    --footer-text: #ffffff;
  }
  * { margin: 0; padding: 0; box-sizing: border-box; }
  html, body {
    width: 927px;
    height: 1200px;
    overflow: hidden;
    background: var(--paper);
  }
  .letterhead {
    position: relative;
    width: 927px;
    height: 1200px;
    background: var(--paper);
    font-family: "Merriweather", Georgia, serif;
  }
  .brand {
    position: absolute;
    top: 52px;
    left: 0;
    width: 100%;
    text-align: center;
    color: var(--brand-red);
    font-weight: 700;
    line-height: 1;
  }
  .brand-name {
    display: block;
    font-size: 44px;
    letter-spacing: -0.5px;
  }
  .brand-tagline {
    display: block;
    margin-top: 6px;
    padding-left: 150px;
    font-size: 9px;
    letter-spacing: 3px;
  }
  .letter-body {
    position: absolute;
    top: 170px;
    left: 90px;
    right: 90px;
    bottom: 90px;
  }
  .footer-band {
    position: absolute;
    left: 0;
    bottom: 0;
    width: 100%;
    height: 58px;
    background: var(--brand-red);
    display: flex;
    align-items: center;
    justify-content: center;
    color: var(--footer-text);
    font-size: 13.5px;
    letter-spacing: 0.3px;
  }
  .footer-band strong { font-weight: 700; }
  .footer-band .divider { margin: 0 6px; }
</style>
</head>
<body>
  <div class="letterhead">
    <header class="brand">
      <span class="brand-name">curtainline</span>
      <span class="brand-tagline">TICKETS</span>
    </header>

    <main class="letter-body"></main>

    <footer class="footer-band">
      <span><strong>24 Hollin Lane,</strong> London, United Kingdom</span>
      <span class="divider">|</span>
      <span>Vat No. <strong>487 2915 06</strong></span>
      <span class="divider">|</span>
      <span><strong>T: 0207 562 3198</strong></span>
    </footer>
  </div>
</body>
</html>
```